Judicial election website to attract voters

I need a simple one-page web design for a judicial election. I'm going to put up one picture, maybe two. The picture I have needs a little touch-up (whiten teeth for example). I have 3 paragraphs of text. I'd like a "Donate" button that can link to a CoinDrift account. I'd also like a little background design, like the Constitution or something like that. There's a couple other little things but that's the bulk of it.

Target Market(s)

Involved voters and some media

Industry/Entity Type

Legal

Number of Pages Required

1 page

Font styles to use
Sans Serif

Requirements
Must have
• My picture, text, donate button
• Phrase "Remember to vote August 30, 2016!"
Nice to have
• Perhaps a second photo, maybe a short 30 second video of me talking directly to the voters, cool background: Constitution, something judgey.
Should not have
• Not sure ... profanity, I guess.

```html
<!DOCTYPE html>
<html lang="en">
<head>
<meta charset="UTF-8">
<title>Local Elections</title>
<link href="https://fonts.googleapis.com/css2?family=Questrial&family=Oswald:wght@500&display=swap" rel="stylesheet">
<style>
  :root {
    --navy: #13245f;
    --red: #c0152f;
    --ink: #333333;
    --soft-bg: #f4f4f4;
    --white: #ffffff;
    --footer-bar: #333333;
  }
  * { margin: 0; padding: 0; box-sizing: border-box; }
  html, body { width: 809px; height: 1200px; overflow: hidden; }
  body {
    position: relative;
    background: var(--white);
    font-family: "Questrial", "Century Gothic", sans-serif;
    color: var(--ink);
  }
  .accent { color: var(--red); }

  .site-header { position: absolute; top: 0; left: 0; width: 809px; height: 76px; }
  .brand {
    position: absolute; font-size: 23px; letter-spacing: 0.3px;
    color: var(--navy); white-space: nowrap; line-height: 1;
  }
  .site-header .brand { left: 66px; top: 26px; }

  .donate-button {
    position: absolute; display: flex; align-items: center; gap: 8px;
    width: 101px; height: 31px; padding-left: 12px;
    background: var(--navy); border-bottom: 2px solid var(--red);
    color: var(--white); font-size: 13px; letter-spacing: 0.4px;
    text-decoration: none;
  }
  .site-header .donate-button { left: 642px; top: 23px; }

  .hero {
    position: absolute; top: 76px; left: 0; width: 809px; height: 323px;
    background: linear-gradient(90deg, #d9d4c8 0%, #c9b79c 30%, #a98863 55%, #c6a078 80%, #b7926b 100%);
  }
  .hero-message {
    position: absolute; left: 470px; top: 124px; width: 300px; text-align: center;
    font-family: "Oswald", "Bebas Neue", sans-serif; font-weight: 500;
    font-size: 31px; line-height: 40px; color: var(--navy);
    text-transform: uppercase;
  }
  .hero-message .date { color: var(--red); display: block; }
  .hero-arrow { position: absolute; top: 216px; }
  .hero-arrow.prev { left: 24px; }
  .hero-arrow.next { left: 764px; }

  .video-section { position: absolute; top: 399px; left: 0; width: 809px; height: 359px; }
  .section-title {
    font-size: 19px; color: var(--navy); letter-spacing: 0.3px; font-weight: 400;
  }
  .video-section .section-title { position: absolute; top: 28px; width: 100%; text-align: center; }
  .video-intro {
    position: absolute; top: 62px; left: 165px; width: 480px;
    text-align: center; font-size: 12.5px; line-height: 17.5px;
  }
  .video-player {
    position: absolute; top: 115px; left: 231px; width: 347px; height: 209px;
    border: 1px solid #cfcfcf; border-radius: 4px; background: var(--white); padding: 3px;
  }
  .video-screen {
    position: relative; width: 100%; height: 100%; border-radius: 3px; overflow: hidden;
    background: #1c1c1c;
  }
  .video-poster {
    position: absolute; inset: 0 0 30px 0;
    background: linear-gradient(120deg, #d97f3a 0%, #7aa3c0 35%, #f2ede4 55%, #c45568 80%, #6b3450 100%);
  }
  .play-badge { position: absolute; left: 151px; top: 78px; }
  .video-controls {
    position: absolute; left: 0; right: 0; bottom: 0; height: 30px;
    background: #1c1c1c; color: var(--white); font-size: 10px;
    display: flex; align-items: center; font-family: Arial, sans-serif;
  }
  .video-controls .play-cell { width: 29px; height: 30px; background: #2c2c2c; display: flex; align-items: center; justify-content: center; }
  .video-controls .time { margin: 0 8px 0 10px; }
  .progress { position: relative; width: 187px; height: 10px; border-radius: 5px; background: #3a3a3a; }
  .progress .played { position: absolute; left: 0; top: 0; width: 84px; height: 10px; border-radius: 5px; background: var(--red); }
  .progress .knob { position: absolute; left: 78px; top: -1px; width: 12px; height: 12px; border-radius: 50%; background: var(--white); }
  .video-controls .total { margin: 0 8px 0 9px; }
  .video-controls svg { margin-right: 9px; }

  .about-section {
    position: absolute; top: 758px; left: 0; width: 809px; height: 347px;
    background: var(--soft-bg);
  }
  .candidate-photo {
    position: absolute; left: 68px; top: 31px; width: 218px; height: 284px;
    background: linear-gradient(180deg, #c9ccd3 0%, #d8c6a6 40%, #e0a890 70%, #e77f5a 100%);
  }
  .about-section .section-title { position: absolute; left: 321px; top: 30px; }
  .about-copy { position: absolute; left: 321px; top: 64px; width: 425px; }
  .about-copy p { font-size: 12.2px; line-height: 17.3px; margin-bottom: 10.5px; }

  .site-footer { position: absolute; top: 1105px; left: 0; width: 809px; height: 66px; }
  .social-links { position: absolute; left: 67px; top: 23px; display: flex; gap: 10px; }
  .social-links span { width: 20px; height: 20px; border-radius: 3px; display: block; }
  .social-links .s1 { background: #3b5a9a; }
  .social-links .s2 { background: #3fb2e6; }
  .social-links .s3 { background: #1a77b5; }
  .social-links .s4 { background: #d2503c; }
  .site-footer .brand { left: 0; width: 809px; text-align: center; top: 25px; font-size: 19px; }
  .site-footer .donate-button { left: 642px; top: 19px; }

  .copyright {
    position: absolute; top: 1171px; left: 0; width: 809px; height: 29px;
    background: var(--footer-bar); color: #e6e6e6; font-size: 8.5px;
    text-align: center; line-height: 29px; letter-spacing: 0.2px;
  }
</style>
</head>
<body>
  <header class="site-header">
    <div class="brand">LOCAL <span class="accent">ELECTIONS</span></div>
    <a class="donate-button" href="#" aria-label="Donate via CoinDrift">
      <svg width="16" height="16" viewBox="0 0 16 16" aria-hidden="true"><circle cx="8" cy="8" r="6.5" fill="none" stroke="#fff" stroke-width="1.6"/></svg>
      DONATE
    </a>
  </header>

  <section class="hero" role="img" aria-label="Photo of voting booths with a voter in the background">
    <svg class="hero-arrow prev" width="22" height="40" viewBox="0 0 22 40" aria-hidden="true"><polyline points="20,1 2,20 20,39" fill="none" stroke="#fff" stroke-width="1.5"/></svg>
    <div class="hero-message">Remember to vote <span class="date">August 30, 2016!</span></div>
    <svg class="hero-arrow next" width="22" height="40" viewBox="0 0 22 40" aria-hidden="true"><polyline points="2,1 20,20 2,39" fill="none" stroke="#fff" stroke-width="1.5"/></svg>
  </section>

  <section class="video-section">
    <h2 class="section-title">WATCH MY <span class="accent">VIDEO</span></h2>
    <p class="video-intro">Lorem ipsum dolor sit amet consectetuer adipiscing elit, sed diam nonummy nibh euismod tincidunt ut laoreet dolore magna aliquam erat volutpat.</p>
    <div class="video-player">
      <div class="video-screen">
        <div class="video-poster" role="img" aria-label="Video still of hands holding an Elections 2016 sign"></div>
        <svg class="play-badge" width="38" height="38" viewBox="0 0 38 38" aria-hidden="true">
          <circle cx="19" cy="19" r="18" fill="#fff" stroke="#ddd"/>
          <polygon points="15,11 27,19 15,27" fill="#111"/>
        </svg>
        <div class="video-controls">
          <div class="play-cell"><svg width="10" height="11" viewBox="0 0 10 11" aria-hidden="true" style="margin:0"><polygon points="1,0 10,5.5 1,11" fill="#fff"/></svg></div>
          <span class="time">04:59</span>
          <div class="progress"><div class="played"></div><div class="knob"></div></div>
          <span class="total">10:35</span>
          <svg width="13" height="12" viewBox="0 0 13 12" aria-hidden="true"><polygon points="0,4 3,4 7,0 7,12 3,8 0,8" fill="#fff"/><path d="M9 3 Q11 6 9 9" stroke="#fff" fill="none"/></svg>
          <svg width="14" height="14" viewBox="0 0 14 14" aria-hidden="true"><path d="M1 1 L13 13 M1 1 H5 M1 1 V5 M13 13 H9 M13 13 V9" stroke="#fff" stroke-width="1.6" fill="none"/></svg>
        </div>
      </div>
    </div>
  </section>

  <section class="about-section">
    <div class="candidate-photo" role="img" aria-label="Portrait photo of the candidate"></div>
    <h2 class="section-title">ABOUT <span class="accent">ME</span></h2>
    <div class="about-copy">
      <p>Lorem ipsum dolor sit amet, consectetuer adipiscing elit, sed diam nonum nibh euismod tincidunt ut laoreet dolore magna aliquam erat volutpat. Ut wisi enim ad minim veniam, quis nostrud exerci tation ullamcorper suscipit lobortis nisl ut aliquip ex ea commodo consequat.</p>
      <p>Lorem ipsum dolor sit amet, consectetuer adipiscing elit, sed diam nonum nibh euismod tincidunt ut laoreet dolore magna aliquam erat volutpat. Ut wisi enim ad minim veniam, quis nostrud exerci tation ullamcorper suscipit lobortis nisl ut aliquip ex ea commodo consequat.</p>
      <p>Lorem ipsum dolor sit amet, consectetuer adipiscing elit, sed diam nonum nibh euismod tincidunt ut laoreet dolore magna aliquam erat volutpat. Ut wisi enim ad minim veniam, quis nostrud exerci tation ullamcorper suscipit lobortis nisl ut aliquip ex ea commodo consequat Lorem ipsum dolor sit amet, consectetuer adipiscing elit, sed diam nonum.</p>
    </div>
  </section>

  <footer class="site-footer">
    <div class="social-links" aria-label="Social links">
      <span class="s1" aria-label="Social link"></span>
      <span class="s2" aria-label="Social link"></span>
      <span class="s3" aria-label="Social link"></span>
      <span class="s4" aria-label="Social link"></span>
    </div>
    <div class="brand">LOCAL <span class="accent">ELECTIONS</span></div>
    <a class="donate-button" href="#" aria-label="Donate via CoinDrift">
      <svg width="16" height="16" viewBox="0 0 16 16" aria-hidden="true"><circle cx="8" cy="8" r="6.5" fill="none" stroke="#fff" stroke-width="1.6"/></svg>
      DONATE
    </a>
  </footer>
  <div class="copyright">COPYRIGHT © 2016 LOCAL ELECTIONS. ALL RIGHTS RESERVED.</div>
</body>
</html>
```